Natural and organic skincare brand needs label design!

I need labels designed for my natural and organic skincare brand velmurine. The front of the bottles must contain the logo (image attached) and the following words: Formulated by a Naturopath; Anti-aging therapy; Organic Facial Oil; with CoEnzyme Q10 and Rosehip Seed Oil; 100ml e3.38fl.oz. Colours I would like used include black/white/grey/silver and aqua. I also like the grey woodgrain used on my draft website (check out www.velmurine.com.au). The logo should be silver foil (shiny).The final design should be simple and communicate nature and sophistication. Some designs I like are found in the attachments. I intend to use black or white bottles.

women aged 30-50 interested in natural products

Skin Care Product

Serif
Sans Serif
Decorative
Script
• Any

• Dimensions: 62mm (w) x 75mm (H) (front label only)
• Must contain the logo (image attached). The logo should be silver foil (shiny). and the following words are to be included on the label:
• Formulated by a Naturopath;
• Anti-aging Therapy;
• Organic Facial Oil;
• with CoEnzyme Q10 and Rosehip Seed Oil;
• 100ml e3.38fl.oz.
• Colours I would like used include black/white/grey/silver and aqua (turquoise). But I am also open to suggestion. I also like the grey woodgrain used on my draft website (check out www.velmurine.com.au)

```html
<!DOCTYPE html>
<html lang="en">
<head>
<meta charset="utf-8">
<title>velmurine – Anti-Aging Therapy label concepts</title>
<link rel="stylesheet" href="https://fonts.googleapis.com/css2?family=Oswald:wght@300;400;500&family=Cormorant+SC:wght@500;600&family=Montserrat:wght@400&display=swap">
<style>
  :root {
    --ink: #0d0d0d;
    --paper: #ffffff;
    --stage: #eeeeee;
    --grey-dark: #2a2a2a;
    --grey-mid: #4a4a4a;
    --grey-light: #d9d9d9;
    --grey-pale: #f1f1f1;
  }
  * { box-sizing: border-box; margin: 0; padding: 0; }
  html, body {
    width: 784px; height: 1200px; overflow: hidden;
    background: var(--stage);
  }
  .labels {
    display: flex; justify-content: center; gap: 44px;
    padding-top: 190px;
  }
  .label {
    position: relative;
    width: 340px; height: 820px;
    background: var(--paper);
    display: flex; flex-direction: column;
    box-shadow: 0 2px 10px rgba(0,0,0,.12);
  }
  .label__field {
    position: relative; height: 600px; overflow: hidden;
  }
  .label__pattern {
    position: absolute; inset: 0;
  }
  .label--dark .label__field { background: var(--ink); }
  .label--dark .label__pattern {
    background:
      radial-gradient(circle at 78% 18%, rgba(120,120,120,.35), transparent 28%),
      radial-gradient(circle at 88% 48%, rgba(110,110,110,.35), transparent 26%),
      radial-gradient(circle at 70% 78%, rgba(100,100,100,.3), transparent 28%),
      linear-gradient(90deg, var(--ink) 30%, var(--grey-dark));
  }
  .label--light .label__field { background: var(--paper); }
  .label--light .label__pattern {
    background:
      radial-gradient(circle at 78% 18%, rgba(190,190,190,.45), transparent 28%),
      radial-gradient(circle at 88% 48%, rgba(200,200,200,.45), transparent 26%),
      radial-gradient(circle at 70% 78%, rgba(190,190,190,.4), transparent 28%),
      linear-gradient(90deg, var(--paper) 30%, var(--grey-pale));
  }
  .brand {
    position: absolute; top: 36px; left: 118px;
    width: 96px; height: 96px; border-radius: 50%;
    display: flex; align-items: center; justify-content: center;
    font-family: "Montserrat", sans-serif; font-size: 15px; letter-spacing: 1px;
  }
  .label--dark .brand { background: var(--paper); color: var(--ink); border: 2px solid var(--grey-light); }
  .label--light .brand { background: var(--ink); color: var(--paper); }
  .title {
    position: absolute; left: 40px; bottom: 20px;
    writing-mode: vertical-rl; transform: rotate(180deg);
    display: flex; flex-direction: row;
  }
  .title__main {
    font-family: "Oswald", sans-serif; font-weight: 400;
    font-size: 60px; line-height: 1; letter-spacing: -.5px;
  }
  .title__sub {
    font-family: "Oswald", sans-serif; font-weight: 300;
    font-size: 27px; line-height: 1.15;
  }
  .label--dark .title { color: var(--paper); }
  .label--light .title { color: var(--ink); }
  .product-type {
    height: 62px; display: flex; align-items: center; justify-content: center;
    font-family: "Oswald", sans-serif; font-weight: 400; font-size: 30px; letter-spacing: .5px;
  }
  .label--dark .product-type { background: var(--ink); color: var(--paper); }
  .label--light .product-type { background: var(--paper); color: var(--ink); }
  .credential {
    height: 90px; display: flex; align-items: center; justify-content: center;
    text-align: center;
    font-family: "Cormorant SC", serif; font-weight: 600; font-size: 27px; line-height: 1.05;
  }
  .label--dark .credential { background: var(--paper); color: var(--ink); }
  .label--light .credential { background: var(--ink); color: var(--paper); }
  .volume {
    flex: 1; display: flex; align-items: center; justify-content: center;
    font-family: "Oswald", sans-serif; font-weight: 300; font-size: 26px; color: var(--ink);
  }
</style>
</head>
<body>
  <main class="labels">
    <article class="label label--dark">
      <div class="label__field">
        <div class="label__pattern" role="img" aria-label="Dark grey floral dahlia pattern on black"></div>
        <div class="brand">velmurine</div>
        <h1 class="title">
          <span class="title__main">ANTI-AGING THERAPY</span>
          <span class="title__sub">with CoEnzyme Q10 and Rosehip Seed Oil</span>
        </h1>
      </div>
      <p class="product-type">ORGANIC FACIAL OIL</p>
      <p class="credential">Formulated by<br>a Naturopath</p>
      <p class="volume">100ml ℮3.38 fl. oz.</p>
    </article>

    <article class="label label--light">
      <div class="label__field">
        <div class="label__pattern" role="img" aria-label="Pale grey floral dahlia pattern on white"></div>
        <div class="brand">velmurine</div>
        <h1 class="title">
          <span class="title__main">ANTI-AGING THERAPY</span>
          <span class="title__sub">with CoEnzyme Q10 and Rosehip Seed Oil</span>
        </h1>
      </div>
      <p class="product-type">ORGANIC FACIAL OIL</p>
      <p class="credential">Formulated by<br>a Naturopath</p>
      <p class="volume">100ml ℮3.38 fl. oz.</p>
    </article>
  </main>
</body>
</html>
```